Business Card for Marco Thieblin Analytics and Marco Thieblin Photography

I want a double sided business card: on one side it should be about "Marco Thieblin Photography" and on the other side about "Marco Thieblin Analytics". You find the logos for these two projects in the attachments. The design of the business card should blend well with the colours and fonts used in the logos and should be quite simple, yet look professional and modern.

In addition to my name, there should be content for a telephone number, e-mail address and website. There should be little icons (for telephone, email and web) before these fields. I do not want a postal mail address field.
Lastly you should indicate that people can contact me in the following languages: Lëtzebuergesch, Deutsch, Français, English, Castellano, Ido
This should be very unobtrusive: either in a small muted font or with little icons (preferably without using flags as flags represent nations, not languages - one possibility would be by using the 2 letter ISO codes).

The design should be delivered in Adobe Illustrator format or something similar that I can edit easily, as it's possible that I will change my e-mail address and domain soon.

I hope this was detailed enough but still leaves you some freedom for designing something nice.

Thank you!
Marco

Industry/Entity Type

Business

Contact Information for Business Card

e-mail address: mtb_@orvenmail.example
website: www.marcothieblin.example (for Marco Thieblin Photography)
website: kelvodata.example/mtb (for Marco Thieblin Analytics - this address is likely to change)
phone: +352 691 987 654 (not my real number - I prefer not to publish it on the web)

Requirements
Nice to have
• A speech bubble followed by the 2-letter language codes (lb, de, fr, en, es, io) or even speech bubble icons for every language would be nice and eliminates the need to put text like 'you can contact me in the following languages'.

```html
<!DOCTYPE html>
<html lang="en">
<head>
<meta charset="utf-8">
<title>Marco Thieblin – Business Cards</title>
<link rel="stylesheet" href="https://fonts.googleapis.com/css2?family=Tinos:wght@400;700&display=swap">
<style>
  :root {
    --stage: #2b2b2b;
    --card-dark: #272526;
    --card-white: #ffffff;
    --accent-orange: #f08a24;
    --accent-yellow: #f5c400;
    --accent-blue: #1aa3e0;
    --accent-green: #7cc043;
    --accent-teal: #1f9e5a;
    --text-light: #f2f2f2;
    --text-dark: #333333;
    --icon-dark: #1d1d1d;
  }
  * { box-sizing: border-box; margin: 0; padding: 0; }
  html, body {
    width: 1200px; height: 852px; overflow: hidden;
    background: var(--stage);
    font-family: "Tinos", "Times New Roman", serif;
  }
  .canvas {
    position: relative; width: 1200px; height: 852px;
    display: flex; align-items: center; justify-content: center; gap: 40px;
  }
  .card {
    position: relative; width: 540px; height: 309px;
    border-radius: 16px; overflow: hidden;
    background: var(--card-white);
    box-shadow: 0 10px 30px rgba(0,0,0,.45);
  }

  /* Brand lockup: plain circle + name */
  .brand {
    position: absolute; left: 0; width: 100%;
    display: flex; justify-content: center; align-items: center; gap: 14px;
  }
  .brand__mark { width: 44px; height: 44px; border-radius: 50%; flex: none; }
  .brand__name {
    font-weight: 400; font-size: 34px; line-height: 1; color: var(--accent-orange);
    white-space: nowrap;
  }

  .contact-row {
    position: absolute; left: 0; width: 100%;
    display: flex; justify-content: center; align-items: center; gap: 16px;
    font-size: 13px; color: var(--text-light);
  }
  .contact-item { display: flex; align-items: center; gap: 6px; white-space: nowrap; }
  .contact-icon { width: 17px; height: 17px; flex: none; }

  /* Photography side */
  .card--photo .card__dark {
    position: absolute; left: 0; top: 0; width: 100%; height: 232px;
    background: var(--card-dark);
  }
  .card--photo .card__edge {
    position: absolute; left: 0; bottom: 0; width: 100%; height: 7px;
    background: var(--accent-yellow);
  }
  .card--photo .brand { top: 62px; }
  .card--photo .brand__mark { background: var(--accent-yellow); }
  .card--photo .contact-row { top: 148px; }
  .languages-note {
    position: absolute; left: 0; top: 184px; width: 100%; text-align: center;
    font-size: 12px; color: var(--text-light);
  }
  .language-list {
    position: absolute; left: 0; top: 206px; width: 100%;
    display: flex; justify-content: center; gap: 8px; list-style: none;
  }
  .language-bubble {
    position: relative; padding: 3px 8px; border-radius: 4px;
    font-size: 11px; color: var(--text-dark); background: var(--bubble);
  }
  .language-bubble::after {
    content: ""; position: absolute; left: 8px; bottom: -5px;
    border-left: 5px solid transparent; border-right: 5px solid transparent;
    border-top: 5px solid var(--bubble);
  }
  .language-bubble--yellow { --bubble: var(--accent-yellow); }
  .language-bubble--blue { --bubble: var(--accent-blue); }
  .language-bubble--green { --bubble: var(--accent-green); }
  .language-bubble--orange { --bubble: var(--accent-orange); }

  /* Analytics side */
  .card--analytics .brand { top: 100px; }
  .card--analytics .brand__mark { background: var(--accent-teal); }
  .card--analytics .card__band {
    position: absolute; left: 0; bottom: 0; width: 100%; height: 56px;
    background: var(--card-dark);
  }
  .card--analytics .contact-row { bottom: 19px; }
</style>
</head>
<body>
<main class="canvas">

  <section class="card card--photo" aria-label="Photography side">
    <div class="card__dark"></div>
    <div class="brand">
      <span class="brand__mark"></span>
      <h1 class="brand__name">Marco Thieblin Photography</h1>
    </div>
    <div class="contact-row">
      <span class="contact-item">
        <svg class="contact-icon" viewBox="0 0 20 20"><circle cx="10" cy="10" r="10" fill="#f5c400"/><path d="M6 7c0-1 1-2 2-1l1 2-1 1c.5 1.2 1.5 2.2 2.7 2.7l1-1 2 1c1 1 0 2-1 2-3.5 0-6.7-3.2-6.7-6.7z" fill="#1d1d1d"/></svg>
        +352 691 987 654
      </span>
      <span class="contact-item">
        <svg class="contact-icon" viewBox="0 0 20 20"><circle cx="10" cy="10" r="10" fill="#f5c400"/><rect x="5" y="6.5" width="10" height="7" fill="none" stroke="#1d1d1d" stroke-width="1.3"/><path d="M5 6.5l5 4 5-4" fill="none" stroke="#1d1d1d" stroke-width="1.3"/></svg>
        mtb_@orvenmail.example
      </span>
      <span class="contact-item">
        <svg class="contact-icon" viewBox="0 0 20 20"><circle cx="10" cy="10" r="10" fill="#f5c400"/><circle cx="10" cy="10" r="5.5" fill="none" stroke="#1d1d1d" stroke-width="1.2"/><path d="M4.5 10h11M10 4.5c-2.5 3-2.5 8 0 11M10 4.5c2.5 3 2.5 8 0 11" fill="none" stroke="#1d1d1d" stroke-width="1"/></svg>
        www.marcothieblin.example
      </span>
    </div>
    <p class="languages-note">You can contact me in the following languages</p>
    <ul class="language-list">
      <li class="language-bubble language-bubble--yellow">Lëtzebuergesch</li>
      <li class="language-bubble language-bubble--blue">Deutsch</li>
      <li class="language-bubble language-bubble--green">Français</li>
      <li class="language-bubble language-bubble--orange">English</li>
      <li class="language-bubble language-bubble--yellow">Castellano</li>
      <li class="language-bubble language-bubble--blue">Ido</li>
    </ul>
    <div class="card__edge"></div>
  </section>

  <section class="card card--analytics" aria-label="Analytics side">
    <div class="brand">
      <span class="brand__mark"></span>
      <h1 class="brand__name">Marco Thieblin Analytics</h1>
    </div>
    <div class="card__band"></div>
    <div class="contact-row">
      <span class="contact-item">
        <svg class="contact-icon" viewBox="0 0 20 20"><circle cx="10" cy="10" r="10" fill="#f08a24"/><path d="M6 7c0-1 1-2 2-1l1 2-1 1c.5 1.2 1.5 2.2 2.7 2.7l1-1 2 1c1 1 0 2-1 2-3.5 0-6.7-3.2-6.7-6.7z" fill="#fff"/></svg>
        +352 691 987 654
      </span>
      <span class="contact-item">
        <svg class="contact-icon" viewBox="0 0 20 20"><circle cx="10" cy="10" r="10" fill="#f08a24"/><rect x="5" y="6.5" width="10" height="7" fill="none" stroke="#fff" stroke-width="1.3"/><path d="M5 6.5l5 4 5-4" fill="none" stroke="#fff" stroke-width="1.3"/></svg>
        mtb_@orvenmail.example
      </span>
      <span class="contact-item">
        <svg class="contact-icon" viewBox="0 0 20 20"><circle cx="10" cy="10" r="10" fill="#f08a24"/><circle cx="10" cy="10" r="5.5" fill="none" stroke="#fff" stroke-width="1.2"/><path d="M4.5 10h11M10 4.5c-2.5 3-2.5 8 0 11M10 4.5c2.5 3 2.5 8 0 11" fill="none" stroke="#fff" stroke-width="1"/></svg>
        kelvodata.example/mtb
      </span>
    </div>
  </section>

</main>
</body>
</html>
```